Workforce Equity Lens Poster for staff

Our organization has developed an equity lens to be used by staff when implementing new programs and services. We need a poster that will be used as a quick reference for staff to use on a daily basis and will hang in cubicles. We'd like the main six questions to stand out with the subsequent questions less prominent. Looking for a poster that is 11 x 17 inches.

Industry/Entity Type

Equity

Font styles to use
Sans Serif

Colors

Designer to choose colors to be used in the design.

Requirements
Must have
• Easy to read. Not too text heavy, so any way to highlight the main six questions. It would be great to have some sort of icon or illustration with each of the six questions.
Nice to have
• Illustrative design features.
Should not have
• No photos of people.

```html
<!DOCTYPE html>
<html lang="en">
<head>
<meta charset="utf-8">
<title>Ridgeline County Workforce System Equity Lens</title>
<link rel="stylesheet" href="https://fonts.googleapis.com/css2?family=Lato:wght@400;700;900&display=swap">
<style>
  :root {
    --brand-blue: #1f64b8;
    --deep-blue: #17509a;
    --ink: #3a3f47;
    --paper: #ffffff;
    --paper-shade: #e4e6ea;
    --icon-fill: #d9dde3;
  }
  * { margin: 0; padding: 0; box-sizing: border-box; }
  html, body { width: 797px; height: 1200px; overflow: hidden; background: #f2f2f2; }
  body { font-family: "Lato", sans-serif; color: var(--ink); }
  .poster {
    position: relative; width: 797px; height: 1200px; overflow: hidden;
    background: linear-gradient(180deg, var(--paper) 0%, var(--paper-shade) 55%);
  }
  .header-band { position: absolute; top: 0; left: 0; width: 797px; height: 150px; }
  .brand {
    position: absolute; top: 38px; right: 40px;
    display: flex; align-items: center; gap: 12px; color: var(--paper);
  }
  .brand-mark { width: 34px; height: 34px; border-radius: 50%; background: var(--paper); }
  .brand-name { font-weight: 700; font-size: 24px; line-height: 1; }
  .intro { position: absolute; top: 160px; left: 48px; right: 48px; }
  .intro h2 { color: var(--brand-blue); font-weight: 900; font-size: 31px; margin-bottom: 8px; }
  .intro p { font-size: 14px; line-height: 1.45; margin-bottom: 12px; }
  .lens-title {
    position: absolute; top: 600px; left: 48px; right: 40px;
    color: var(--brand-blue); font-weight: 900; font-size: 28px; text-align: right;
  }
  .lens-panel { position: absolute; top: 570px; left: 0; width: 797px; height: 630px; }
  .questions { position: absolute; top: 660px; left: 40px; right: 44px; list-style: none; }
  .question { display: flex; align-items: center; gap: 22px; height: 88px; color: var(--paper); }
  .question-icon {
    flex: 0 0 70px; height: 70px; border-radius: 50%;
    background: var(--icon-fill); border: 4px solid var(--paper);
  }
  .question-text { font-size: 15px; line-height: 1.35; }
  .question-text strong { font-weight: 900; text-transform: uppercase; font-size: 16px; }
</style>
</head>
<body>
<div class="poster">
  <svg class="header-band" viewBox="0 0 797 150" aria-hidden="true">
    <polygon points="0,0 797,0 797,120 250,120 200,96 0,96" fill="var(--brand-blue)"/>
    <polygon points="0,96 200,96 250,120 0,120" fill="var(--deep-blue)" opacity="0.35"/>
  </svg>
  <div class="brand">
    <span class="brand-mark"></span>
    <span class="brand-name">Ridgeline Workforce Partnership</span>
  </div>

  <section class="intro">
    <h2>What is equity?</h2>
    <p>In workforce development, equity is the notion that everyone has the opportunity to obtain quality, living wage employment or be placed in employment-related training regardless of their national origin, race, gender, sexual orientation, disability, first language or other distinguishing characteristic. Different approaches to delivery of workforce services may be necessary in order for each customer to achieve success in training or employment.</p>
    <h2>What is an equity lens?</h2>
    <p>An equity lens is a practical tool that will help ensure that policies, programs, decisions, or proposed actions in Ridgeline County's workforce system result in equitable outcomes for all job seekers. This lens shall be used by the Ridgeline Workforce Partnership Board of Directors and Executive Board when making policy decisions or decisions on how to allocate funding. It shall also be used by Ridgeline Workforce Partnership staff, JobPoint Ridgeline staff, and other workforce system partners when creating and implementing programs.</p>
    <p>The purpose of the equity lens is to provide a tool to assist the Board and staff with identifying potentially negative outcomes for policies, programs, decisions, or actions that could increase disparities for under-represented populations. An equity lens is not meant to be a road block to effectively delivering workforce services, but rather a mechanism to identify and remove systemic barriers for under-represented populations as it relates to workforce-related services.</p>
  </section>

  <svg class="lens-panel" viewBox="0 0 797 630" aria-hidden="true">
    <path d="M0,75 L700,75 Q760,75 797,40 L797,630 L0,630 Z" fill="var(--brand-blue)"/>
  </svg>
  <h1 class="lens-title">Ridgeline County Workforce System Equity Lens</h1>

  <ul class="questions">
    <li class="question">
      <span class="question-icon" role="img" aria-label="Clipboard checklist icon"></span>
      <p class="question-text"><strong>Who is affected?</strong> Who are the groups affected by this policy, metric, program, decision, or proposed action? How will each group be affected? Is any group negatively affected in a disproportionate way?</p>
    </li>
    <li class="question">
      <span class="question-icon" role="img" aria-label="People seated around a table icon"></span>
      <p class="question-text"><strong>Are they at the table?</strong> How have you actively involved stakeholders who are also members of the communities affected by the policy, metric, program, decision, or proposed action?</p>
    </li>
    <li class="question">
      <span class="question-icon" role="img" aria-label="Road barrier icon"></span>
      <p class="question-text"><strong>What are the barriers?</strong> What are the societal or organizational barriers that prevent a population from being successful?</p>
    </li>
    <li class="question">
      <span class="question-icon" role="img" aria-label="Strategy plan diagram icon"></span>
      <p class="question-text"><strong>What are population-specific strategies?</strong> To address any inequities, do we have solutions that are tailored to work for the disproportionately affected groups? Have we used the 'Platinum Rule'?</p>
    </li>
    <li class="question">
      <span class="question-icon" role="img" aria-label="Broken tree branch icon"></span>
      <p class="question-text"><strong>Are there unintended consequences?</strong> Does this policy, program, decision, or proposed action ignore or worsen existing disparities or produce other unintended consequences?</p>
    </li>
    <li class="question">
      <span class="question-icon" role="img" aria-label="Thumbs up and thumbs down icon"></span>
      <p class="question-text"><strong>How do we measure success in a population-specific way?</strong> Describe how data about the policy, metric, program, decision, or proposed action, and its impact (positive or negative) on equitable access and outcomes, will be monitored and evaluated?</p>
    </li>
  </ul>
</div>
</body>
</html>
```